Hall of Fame annnouncement graphic for social media

I need a social media Hall of Fame announcement designed in the styles of some of the examples I've posted. I have attached the two gentlemens head shots ... the names are Dale Prosser and Jim Harnden

It is for the BRIARWOOD LINKS HONOR SOCIETY also include 2026 Inductees ... I have also attached the logo... make the post in similar colors as the logo.

I need this tomorrow so I am going to pick a winner in the next 24 hours.

```html
<!DOCTYPE html>
<html lang="en">
<head>
<meta charset="utf-8">
<title>Briarwood Links Honor Society – 2026 Inductees</title>
<link rel="stylesheet" href="https://fonts.googleapis.com/css2?family=Figtree:wght@400;800&display=swap">
<style>
  :root {
    --navy: #1f354c;
    --paper: #fdfdfd;
    --gold: #f9c623;
    --label-blue: #0a7bc4;
    --white: #ffffff;
  }
  * { margin: 0; padding: 0; box-sizing: border-box; }
  html, body {
    width: 1200px; height: 725px; overflow: hidden;
    background: var(--paper);
  }
  .announcement {
    position: relative; width: 1200px; height: 725px;
    background: var(--paper); overflow: hidden;
  }
  .band {
    position: absolute; left: 0; top: 89px;
    width: 1200px; height: 493px;
    background: var(--navy);
  }
  .society-name {
    position: absolute; left: 0; top: 196px; width: 922px;
    text-align: center;
    font-family: "Figtree", sans-serif; font-weight: 800;
    font-size: 68px; line-height: 1.12; letter-spacing: 1px;
    color: var(--white);
  }
  .year-line {
    position: absolute; left: 0; top: 443px; width: 922px;
    text-align: center;
    font-family: "Figtree", sans-serif; font-weight: 400;
    font-size: 54px; color: var(--gold); letter-spacing: -0.5px;
  }
  .portrait {
    position: absolute;
    border: 2px solid var(--white);
    border-bottom-right-radius: 16px;
  }
  .portrait--prosser {
    left: 938px; top: 49px; width: 174px; height: 212px;
    background: linear-gradient(180deg, #e9e1d8 0%, #e3cbb8 45%, #f1f1f2 75%, #f6f6f7 100%);
  }
  .portrait--harnden {
    left: 932px; top: 357px; width: 176px; height: 212px;
    background: linear-gradient(180deg, #e6ecf1 0%, #dde4ea 35%, #4f6a3c 60%, #7d9a57 80%, #8fa863 100%);
  }
  .name-tag {
    position: absolute; height: 58px;
    background: var(--label-blue);
    color: var(--white);
    font-family: "Figtree", sans-serif; font-weight: 800;
    font-size: 30px; line-height: 58px; text-align: center;
    letter-spacing: -0.3px; white-space: nowrap;
  }
  .name-tag--prosser { left: 917px; top: 260px; width: 219px; }
  .name-tag--harnden { left: 914px; top: 569px; width: 219px; }
</style>
</head>
<body>
<main class="announcement">
  <div class="band"></div>

  <h1 class="society-name">BRIARWOOD LINKS<br>HONOR SOCIETY</h1>

  <p class="year-line">2026 Inductees</p>

  <div class="portrait portrait--prosser" role="img" aria-label="Headshot of inductee Dale Prosser"></div>
  <p class="name-tag name-tag--prosser">Dale Prosser</p>

  <div class="portrait portrait--harnden" role="img" aria-label="Photo of inductee Jim Harnden on a golf course"></div>
  <p class="name-tag name-tag--harnden">Jim Harnden</p>
</main>
</body>
</html>
```